professional looking data specialist website

I've recently had a new logo designed and I'm now looking to get a professional looking website built. This is for a new company that specialises in data. We look to support companies with business intelligence, report modelling, data governance to new european legislation (GDPR). We are offer consultancy or we can attend site and complete work when required. Our target arket is united kingdom wide and we are specifically aiming at small to medium sized companies.

Target Market(s)

small to medium enterprise companies from all industries

Industry/Entity Type

Professional Service

Coding

Coded - Design and coding required

Number of Pages Required

4 page

Font styles to use
Sans Serif

Colors

Designer to choose colors to be used in the design.

Requirements
Must have
• Professional look including the company logo, need to have ability to request more information from us so needs a inquiries page, seperate pages for the different offerings, data governance, report modelling, business intelligence implementation, data protection
Nice to have
• any website interaction, animation, etc
Should not have
• too many colours, too busy pages, must look professional

```html
<!DOCTYPE html>
<html lang="en">
<head>
<meta charset="utf-8">
<title>Quillmere Data Ltd</title>
<link href="https://fonts.googleapis.com/css2?family=Oswald:wght@500;600&family=Roboto+Condensed:wght@400;700&family=Roboto:wght@400;500;700&display=swap" rel="stylesheet">
<style>
:root{
  --blue:#1a6fc4;
  --blue-dark:#0f5aa8;
  --blue-deep:#0b4a8f;
  --ink:#222;
  --text:#555;
  --muted:#9a9a9a;
  --light:#f1f1f1;
  --line:#ddd;
  --dark:#2b2b2b;
  --footer:#1e1e1e;
  --white:#fff;
}
*{box-sizing:border-box;margin:0;padding:0}
html,body{width:1200px;height:3197px;overflow:hidden}
body{font-family:"Roboto",Arial,sans-serif;color:var(--text);background:var(--white);position:relative}
.section{position:absolute;left:0;width:1200px}
p{font-size:11px;line-height:16px}

.topbar{top:0;height:20px}
.topbar .tab{position:absolute;right:150px;top:0;height:18px;background:#e9e9e9;border-radius:0 0 8px 8px;display:flex;gap:22px;padding:0 22px;align-items:center;font-size:10px;color:#444}
.topbar .tab span::before{content:"";display:inline-block;width:6px;height:6px;background:#555;margin-right:5px;border-radius:1px}
.header{top:0;height:94px;border-bottom:1px solid #eee}
.brand{position:absolute;left:160px;top:50px;display:flex;align-items:center;gap:8px;font-weight:700;font-size:21px;color:var(--blue-deep)}
.brand .mark{width:18px;height:18px;background:var(--blue)}
.nav{position:absolute;right:160px;top:53px;display:flex;gap:23px;font-size:11.5px;font-weight:500;color:#333}
.nav .active{color:var(--blue)}

.hero{top:94px;height:496px;background:linear-gradient(100deg,#8e8f8b 0%,#cfcfcc 30%,#e4e4e2 55%,#9a9896 80%,#6e6c6a 100%)}
.hero .tag{position:absolute;left:633px;top:247px;background:var(--blue);color:var(--white);font-family:"Roboto Condensed",sans-serif;font-size:17px;padding:5px 12px;letter-spacing:.3px}
.hero .head{position:absolute;left:630px;top:283px;background:var(--white);color:var(--ink);font-family:"Roboto Condensed",sans-serif;font-weight:700;font-size:26px;padding:8px 14px}

.services{top:590px;height:337px;background:linear-gradient(180deg,#1b6ec0,#1561b2)}
.svc{position:absolute;top:37px;width:210px;height:260px;border:2px solid rgba(255,255,255,.45);text-align:center;color:var(--white)}
.svc .ico{width:78px;height:78px;border-radius:50%;background:rgba(255,255,255,.35);margin:26px auto 0;display:flex;align-items:center;justify-content:center}
.svc h3{font-family:"Roboto Condensed",sans-serif;font-size:13px;font-weight:700;margin-top:20px;color:#cfe3ff;letter-spacing:.3px;line-height:15px;min-height:30px;display:flex;align-items:center;justify-content:center;padding:0 12px}
.svc p{font-size:10px;line-height:13px;color:#bcd6f3;margin:6px 14px 0}
.btn-ghost{display:inline-block;border:1px solid rgba(255,255,255,.7);font-size:9px;font-weight:700;color:var(--white);padding:6px 10px;margin-top:10px}

.welcome{top:927px;height:362px;text-align:center}
.welcome h2{font-family:"Oswald",sans-serif;font-weight:500;font-size:31px;color:var(--ink);margin-top:48px}
.welcome .sub{font-size:10px;color:var(--muted);margin-top:2px}
.divider{position:absolute;left:162px;width:876px;top:142px;height:1px;background:var(--line)}
.divider .sq{position:absolute;left:428px;top:-14px;width:20px;height:20px;background:var(--blue);border:4px solid var(--white);box-sizing:content-box}
.welcome .body{position:absolute;left:162px;top:176px;width:876px;font-size:10.5px;line-height:16px;color:#444}
.btn-outline{display:inline-block;border:2px solid #cfcfcf;font-size:10px;font-weight:700;color:#333;padding:8px 16px}
.welcome .btn-outline{position:absolute;left:543px;top:268px}

.who{top:1289px;height:309px;background:var(--light)}
.who .photo{position:absolute;left:0;top:0;width:597px;height:309px;background:linear-gradient(120deg,#c9ccd0,#8a8f96 55%,#e6e7e8)}
.who h2{position:absolute;left:636px;top:42px;font-family:"Oswald",sans-serif;font-weight:500;font-size:23px;color:var(--ink)}
.who p{position:absolute;left:636px;top:88px;width:402px;font-size:10.5px;line-height:15.5px;color:#444;text-align:justify}
.who .btn-outline{position:absolute;left:638px;top:236px;background:var(--white)}

.quote{top:1598px;height:192px;background:linear-gradient(90deg,#303030,#262626 60%,#3a3a3a)}
.field{position:absolute;width:188px;height:32px;background:#bdbdbd;border:1px solid #d6d6d6;font-size:9px;color:#666;padding:10px 10px}
.quote .go{position:absolute;left:162px;top:128px;width:188px;height:30px;background:var(--blue);color:var(--white);font-size:10.5px;font-weight:700;text-align:center;line-height:30px}
.quote .qmark{position:absolute;left:978px;top:40px}
.quote .kick{position:absolute;right:162px;top:101px;color:var(--white);font-family:"Roboto Condensed",sans-serif;font-weight:700;font-size:14px;text-align:right}
.quote .big{position:absolute;right:162px;top:120px;color:var(--white);font-family:"Roboto Condensed",sans-serif;font-weight:700;font-size:30px;text-align:right}

.why{top:1790px;height:441px}
.why h2{text-align:center;font-family:"Roboto Condensed",sans-serif;font-weight:700;font-size:30px;color:var(--ink);margin-top:38px}
.uline{width:40px;height:4px;background:var(--blue);margin:6px auto 0}
.pt{position:absolute;width:310px}
.pt h4{font-family:"Roboto Condensed",sans-serif;font-size:13px;font-weight:700;color:var(--ink);margin-bottom:6px}
.pt p{font-size:10.5px;line-height:14.5px;color:#444}
.pt .more{display:block;font-size:9.5px;font-weight:700;color:var(--blue);margin-top:6px}
.pt.left{text-align:right}
.num{position:absolute;width:86px;height:86px;border-radius:50%;background:var(--blue);border:5px solid #fff;box-shadow:0 0 0 3px var(--blue);color:var(--white);font-family:"Roboto Condensed",sans-serif;font-size:34px;display:flex;align-items:center;justify-content:center}

.reach{top:2231px;height:245px;background:linear-gradient(110deg,#1f74c6,#1762b0 60%,#3a85cf);text-align:center;color:var(--white)}
.reach h2{font-family:"Roboto Condensed",sans-serif;font-weight:700;font-size:27px;margin-top:62px}
.reach p{font-size:12px;margin-top:8px;color:#e2eefb}
.reach .btn{display:inline-block;background:#1c1c1c;color:var(--white);font-size:12px;font-weight:700;padding:12px 28px;margin-top:22px}

.clients{top:2476px;height:328px}
.clients h2{text-align:center;font-family:"Roboto Condensed",sans-serif;font-weight:700;font-size:24px;color:var(--ink);margin-top:42px}
.clients h2 span{color:var(--blue)}
.cl-photo{position:absolute;top:128px;width:217px;height:145px}
.cl{position:absolute;top:130px;width:186px}
.cl h3{font-family:"Roboto Condensed",sans-serif;font-size:19px;font-weight:400;color:var(--ink);letter-spacing:.4px}
.cl .role{font-size:10px;color:var(--blue);margin:2px 0 10px}
.cl p{font-size:10.5px;line-height:14.5px;color:#444}

.news{top:2804px;height:200px;background:var(--light);text-align:center}
.news h2{font-family:"Roboto Condensed",sans-serif;font-weight:700;font-size:25px;color:var(--ink);margin-top:30px}
.news .lead{font-size:9.5px;color:#555;margin-top:8px}
.nf{position:absolute;top:122px;height:33px;background:var(--white);border:1px solid #d8d8d8;font-size:9px;color:#999;text-align:left;padding:11px 10px}
.news .sub-btn{position:absolute;left:878px;top:122px;width:160px;height:33px;background:var(--blue);color:var(--white);font-size:11px;font-weight:700;line-height:33px}

.footer{top:3004px;height:150px;background:var(--footer);color:#cfcfcf}
.fcol{position:absolute;top:46px}
.fcol h4{display:flex;align-items:center;gap:7px;font-size:11.5px;font-weight:700;color:var(--white);margin-bottom:22px}
.fcol p{font-size:11px;line-height:17px;color:#bbb}
.bottom{top:3154px;height:43px;background:var(--blue)}
.flinks{position:absolute;left:162px;top:15px;display:flex;gap:13px;font-size:10.5px;color:var(--white)}
.social{position:absolute;right:162px;top:9px;display:flex;gap:6px}
.social span{width:22px;height:22px;border-radius:50%;border:1.5px solid var(--white)}
</style>
</head>
<body>

<header class="section header">
  <div class="brand"><span class="mark"></span>Quillmere Data Ltd</div>
  <nav class="nav">
    <span class="active">HOME</span><span>ABOUT US</span><span>SERVICES</span><span>DATA</span><span>FEATURES</span><span>BLOG</span><span>PARTNERS</span><span>CONTACT US</span>
  </nav>
</header>
<div class="section topbar"><div class="tab"><span>Home</span><span>Login</span><span>Register</span></div></div>

<section class="section hero" role="img" aria-label="Photo of a smiling consultant working at a laptop in a bright office">
  <div class="tag">WE ARE SPECIALISTS IN DATA</div>
  <div class="head">OVER 25 YEARS OF EXPERIENCE</div>
</section>

<section class="section services">
  <div class="svc" style="left:162px">
    <div class="ico"><svg width="40" height="40" viewBox="0 0 40 40" fill="#1a3f73"><rect x="6" y="8" width="7" height="24"/><rect x="15" y="8" width="7" height="24"/><rect x="24" y="10" width="7" height="22" transform="rotate(-12 27 21)"/></svg></div>
    <h3>DATA GOVERNANCE</h3>
    <p>Lorem Ipsum is simply dummy text industry's standard dummy text ever since printer took</p>
    <span class="btn-ghost">READ MORE ➜</span>
  </div>
  <div class="svc" style="left:384px">
    <div class="ico"><svg width="40" height="40" viewBox="0 0 40 40" fill="none" stroke="#1a3f73" stroke-width="3"><rect x="7" y="9" width="26" height="22"/><line x1="11" y1="15" x2="29" y2="15"/><line x1="11" y1="20" x2="19" y2="20"/><line x1="11" y1="25" x2="19" y2="25"/><rect x="22" y="19" width="7" height="7" fill="#1a3f73"/></svg></div>
    <h3>REPORT MODELLING</h3>
    <p>Lorem Ipsum is simply dummy text industry's standard dummy text ever since printer took</p>
    <span class="btn-ghost">READ MORE ➜</span>
  </div>
  <div class="svc" style="left:605px">
    <div class="ico"><svg width="40" height="40" viewBox="0 0 40 40" fill="#1a3f73"><rect x="7" y="24" width="5" height="9"/><rect x="15" y="19" width="5" height="14"/><rect x="23" y="22" width="5" height="11"/><rect x="31" y="14" width="5" height="19"/><polyline points="6,20 15,12 22,16 33,6" fill="none" stroke="#1a3f73" stroke-width="2.5"/></svg></div>
    <h3>BUSINESS INTELLIGENCE IMPLEMENTATION</h3>
    <p>Lorem Ipsum is simply dummy text industry's standard printer took</p>
    <span class="btn-ghost">READ MORE ➜</span>
  </div>
  <div class="svc" style="left:826px">
    <div class="ico"><svg width="40" height="40" viewBox="0 0 40 40" fill="#1a3f73"><ellipse cx="18" cy="10" rx="11" ry="4"/><path d="M7 13v5c0 2 5 4 11 4s11-2 11-4v-5c0 2-5 4-11 4S7 15 7 13z"/><path d="M7 21v5c0 2 5 4 11 4v-8c-6 0-11-1-11-1z"/><rect x="23" y="24" width="11" height="9"/><path d="M25 24v-3a3.5 3.5 0 0 1 7 0v3" fill="none" stroke="#1a3f73" stroke-width="2"/></svg></div>
    <h3>DATA PROTECTION</h3>
    <p>Lorem Ipsum is simply dummy text industry's standard dummy text ever since printer took</p>
    <span class="btn-ghost">READ MORE ➜</span>
  </div>
</section>

<section class="section welcome">
  <h2>WELCOME TO QUILLMERE DATA LTD</h2>
  <div class="sub">Lorem Ipsum is simply dummy text typesetting industry</div>
  <div class="divider"><span class="sq"></span></div>
  <p class="body">Lorem Ipsum is simply dummy text of the printing and typesetting industry. Lorem Ipsum has been the industry's standard dummy text ever since the 1500s, when an unknown printer took a galley of type and scrambled it to make a type specimen book. It has survived not only five centuries, but also the leap into electronic typesetting, remaining essentially unchanged. It was popularised in the 1960s with the release of transfer sheets containing Lorem Ipsum passages, and more recently with desktop publishing and layout software including versions of Lorem Ipsum.Lorem Ipsum is simply dummy text</p>
  <span class="btn-outline">READ MORE ➜</span>
</section>

<section class="section who">
  <div class="photo" role="img" aria-label="Photo of a business team meeting around a table with laptops and papers"></div>
  <h2>WHO WE ARE</h2>
  <p>Lorem Ipsum is simply dummy text of the printing and typesetting industry. Lorem Ipsum has been the industry's standard dummy text ever since the 1500s, when an unknown printer took a galley of type and scrambled it to make a type specimen release in desktop layout software including versions of Lorem Ipsum.Lorem Ipsum is simply dummy text of the printing and typesetting industry. specimen book. It has survived not only five centuries, but also the leap into electronic Ipsum.Lorem Ipsum is simply dummy text of the printing book.</p>
  <span class="btn-outline">READ MORE ➜</span>
</section>

<section class="section quote">
  <div class="field" style="left:162px;top:43px">Name / Company Name</div>
  <div class="field" style="left:358px;top:43px">Email</div>
  <div class="field" style="left:554px;top:43px">Phone Number</div>
  <div class="field" style="left:162px;top:85px">Number Of Employees</div>
  <div class="field" style="left:358px;top:85px">Number Of Outgoing Invoice</div>
  <div class="field" style="left:554px;top:85px">Number Of Incoming Invoice</div>
  <div class="go">GET A FREE QUOTE ➞</div>
  <svg class="qmark" width="60" height="48" viewBox="0 0 60 48" fill="#fff"><path d="M4 4h22v22c0 11-6 18-16 20l-2-6c6-2 8-6 8-11H4z"/><path d="M34 4h22v22c0 11-6 18-16 20l-2-6c6-2 8-6 8-11H34z"/></svg>
  <div class="kick">GET INQUIRIES</div>
  <div class="big">FOR OUR SERVICES</div>
</section>

<section class="section why">
  <h2>WHY CHOOSE QUILLMERE DATA LTD?</h2>
  <div class="uline"></div>
  <div class="pt left" style="left:163px;top:145px">
    <h4>PROVEN RECORD OF RESULTS</h4>
    <p>Lorem Ipsum is simply dummy text of the printing and typesetting industry. Lorem Ipsum has been the industry's standard dummy text ever since the 1500s, when an unknown printer took a galley more recently with desktop publishing and layout tools</p>
    <span class="more">READ MORE ⟶</span>
  </div>
  <div class="num" style="left:494px;top:141px">01</div>
  <div class="num" style="left:614px;top:141px">02</div>
  <div class="pt" style="left:722px;top:145px">
    <h4>YEARS OF EXPERIENCE</h4>
    <p>Lorem Ipsum is simply dummy text of the printing and typesetting industry. Lorem Ipsum has been the industry's standard dummy text ever since the 1500s, when an unknown printer took a galley more recently with desktop publishing and layout tools.</p>
    <span class="more">READ MORE ⟶</span>
  </div>
  <div class="pt left" style="left:163px;top:284px">
    <h4>STRATEGIC AND AGGRESSIVE</h4>
    <p>Lorem Ipsum is simply dummy text of the printing and typesetting industry. Lorem Ipsum has been the industry's standard dummy text ever since the 1500s, when an unknown printer took a galley more recently with desktop publishing and layout tools</p>
    <span class="more">READ MORE ⟶</span>
  </div>
  <div class="num" style="left:494px;top:280px">03</div>
  <div class="num" style="left:614px;top:280px">04</div>
  <div class="pt" style="left:722px;top:284px">
    <h4>SMALL TO MEDIUM ENTERPRISE</h4>
    <p>Lorem Ipsum is simply dummy text of the printing and typesetting industry. Lorem Ipsum has been the industry's standard dummy text ever since the 1500s, when an unknown printer took a galley more recently with desktop publishing and layout tools.</p>
    <span class="more">READ MORE ⟶</span>
  </div>
</section>

<section class="section reach">
  <h2>REACH YOUR POTENTIAL FASTER AND WITH EASE</h2>
  <p>We will take care of your comapany data and administrative services and take the load off you.</p>
  <span class="btn">GET A QUOTE</span>
</section>

<section class="section clients">
  <h2>CLIENTS THAT <span>TRUST</span> US</h2>
  <div class="cl-photo" style="left:162px;background:linear-gradient(120deg,#e9eaec,#a9adb3 50%,#4a4e55)" role="img" aria-label="Photo of two colleagues reviewing documents at a desk"></div>
  <div class="cl" style="left:405px">
    <h3>DANIEL ASHBY</h3>
    <div class="role">Brindle Co CEO</div>
    <p>Lorem Ipsum is simply dummy text printing and typesetting industry. Lorem Ipsum has been the industry's standard dummy text to make a type specimen book.</p>
  </div>
  <div class="cl-photo" style="left:616px;background:linear-gradient(120deg,#dfe6ee,#b8c4d1 50%,#4f5a68)" role="img" aria-label="Photo of a presenter at a whiteboard in front of an audience"></div>
  <div class="cl" style="left:852px">
    <h3>HELEN MARSH</h3>
    <div class="role">Larkway Group CEO</div>
    <p>Lorem Ipsum is simply dummy text printing and typesetting industry. Lorem Ipsum has been the industry's standard dummy text to make a type specimen book.</p>
  </div>
</section>

<section class="section news">
  <h2>SUBSCRIBE TO OUR NEWSLETTER</h2>
  <p class="lead">If you want to receive monthly updates from us just pop your email in the box.</p>
  <div class="nf" style="left:162px;width:349px">Enter your name</div>
  <div class="nf" style="left:526px;width:337px">Enter your eamil address</div>
  <div class="sub-btn">SUBSCRIBE NOW</div>
</section>

<footer class="section footer">
  <div class="fcol" style="left:162px">
    <h4><svg width="11" height="14" viewBox="0 0 11 14" fill="#fff"><path d="M5.5 0A5.5 5.5 0 0 0 0 5.5C0 9.5 5.5 14 5.5 14S11 9.5 11 5.5A5.5 5.5 0 0 0 5.5 0zm0 7.8a2.3 2.3 0 1 1 0-4.6 2.3 2.3 0 0 1 0 4.6z"/></svg>OUR ADDRESS</h4>
    <p>48 Harrow Lane<br>Leeds, United Kingdom</p>
  </div>
  <div class="fcol" style="left:528px">
    <h4><svg width="15" height="11" viewBox="0 0 15 11" fill="none" stroke="#fff" stroke-width="1.5"><rect x="1" y="1" width="13" height="9"/><polyline points="1,1 7.5,6 14,1"/></svg>CONTACT US</h4>
    <p>+44 113 496 0000<br>hello@quillmeredata.example</p>
  </div>
  <div class="fcol" style="left:878px">
    <h4><svg width="13" height="13" viewBox="0 0 13 13" fill="none" stroke="#fff" stroke-width="1.5"><circle cx="6.5" cy="6.5" r="5.5"/><polyline points="6.5,3 6.5,6.5 9,8"/></svg>OFFICE HOURS</h4>
    <p>Monday to Friday: 8:00 - 17:00<br>Saturday, Sunday: 9:00 - 14:00</p>
  </div>
</footer>

<div class="section bottom">
  <div class="flinks"><span>About Us</span><span>Services</span><span>Data</span><span>Features</span><span>Blog</span><span>Partners</span><span>Contact us</span></div>
  <div class="social"><span></span><span></span><span></span><span></span><span></span></div>
</div>

</body>
</html>
```